Postcard that needs a professional designer to create a great looking postcard

Direct mail postcard designed using the copy and graphics we have supplied. We need it to look professional, clean and eye catching.
We are marketing to builders who need to hire us to build the closets and storage in the homes they are contracted to build.

```html
<!DOCTYPE html>
<html lang="en">
<head>
<meta charset="UTF-8">
<title>Harbor Closets – Builder Postcard</title>
<link rel="stylesheet" href="https://fonts.googleapis.com/css2?family=Oswald:wght@600;700&family=Open+Sans:wght@400;600&display=swap">
<style>
  :root {
    --brand-red: #c8141c;
    --brand-navy: #0f1a45;
    --heading-navy: #1a2060;
    --text-dark: #1c1c1c;
    --white: #ffffff;
    --panel-white: rgba(255, 255, 255, 0.86);
  }
  * { margin: 0; padding: 0; box-sizing: border-box; }
  html, body { width: 1200px; height: 700px; overflow: hidden; background: #ffffff; }
  .postcard {
    position: relative;
    width: 1200px;
    height: 700px;
    overflow: hidden;
    font-family: "Open Sans", Arial, sans-serif;
  }
  .wardrobe-photo {
    position: absolute;
    left: 343px; top: 0;
    width: 857px; height: 632px;
    background:
      radial-gradient(ellipse 180px 260px at 270px 300px, #e8c6b0 0%, rgba(232,198,176,0) 100%),
      linear-gradient(90deg, #7a5548 0%, #c9b4a8 22%, #e9dcd3 45%, #d8c2b3 70%, #b79a82 100%);
  }
  .intro-panel {
    position: absolute;
    left: 0; top: 0;
    width: 343px; height: 632px;
    background: var(--brand-red);
    color: var(--white);
    text-align: center;
  }
  .intro-title {
    font-family: "Oswald", "Arial Narrow", sans-serif;
    font-weight: 700;
    font-size: 56px;
    line-height: 62px;
    margin-top: 40px;
    letter-spacing: 0.5px;
  }
  .intro-copy {
    font-size: 20.5px;
    line-height: 36.5px;
    margin: 58px 28px 0 34px;
  }
  .offer-box {
    position: absolute;
    left: 721px; top: 58px;
    width: 432px; height: 516px;
    background: var(--panel-white);
  }
  .offer-headline {
    font-family: "Oswald", "Arial Narrow", sans-serif;
    font-weight: 700;
    color: var(--brand-red);
    font-size: 41px;
    text-align: center;
    margin-top: 8px;
    line-height: 54px;
  }
  .offer-question {
    font-family: "Oswald", "Arial Narrow", sans-serif;
    font-weight: 700;
    color: var(--heading-navy);
    font-size: 29px;
    line-height: 37px;
    text-align: center;
    margin: 8px 14px 0 14px;
  }
  .needs-list {
    list-style: none;
    margin: 20px 16px 0 78px;
    color: var(--text-dark);
    font-size: 21px;
    line-height: 29px;
  }
  .needs-list li {
    position: relative;
    padding-left: 20px;
  }
  .needs-list li::before {
    content: "•";
    position: absolute;
    left: 2px;
  }
  .call-line {
    margin: 4px 0 0 73px;
    color: var(--text-dark);
    font-size: 21px;
    line-height: 29px;
  }
  .brand-card {
    position: absolute;
    left: 427px; top: 394px;
    width: 306px; height: 197px;
    background: var(--white);
    display: flex;
    flex-direction: column;
    align-items: center;
    justify-content: center;
    gap: 14px;
  }
  .brand-mark {
    width: 64px; height: 64px;
    border-radius: 50%;
    background: var(--brand-red);
  }
  .brand-name {
    font-family: "Open Sans", Arial, sans-serif;
    font-weight: 600;
    color: var(--heading-navy);
    font-size: 25px;
    line-height: 30px;
    text-align: center;
  }
  .phone-bar {
    position: absolute;
    left: 0; top: 632px;
    width: 343px; height: 68px;
    background: var(--brand-red);
    display: flex;
    align-items: center;
    padding-left: 38px;
    gap: 12px;
    color: var(--white);
    font-size: 31px;
  }
  .web-bar {
    position: absolute;
    left: 343px; top: 632px;
    width: 857px; height: 68px;
    background: var(--brand-navy);
    display: flex;
    align-items: center;
    padding-left: 33px;
    gap: 18px;
    color: var(--white);
    font-size: 31px;
  }
  .icon-badge { width: 46px; height: 46px; flex: none; }
</style>
</head>
<body>
<div class="postcard">
  <div class="wardrobe-photo" role="img" aria-label="Smiling woman in a white top with arms crossed, standing in front of a wardrobe of hanging shirts and shelves of folded sweaters"></div>

  <section class="intro-panel">
    <h1 class="intro-title">CALL ON OUR<br>EXPERIENCE</h1>
    <p class="intro-copy">Trying to provide top quality craftsman built Closets and Storage Systems for your homeowner is often frustrating and time consuming.<br>For a satisfied homeowner simply call on our 15 years experience to complete your clients closets on time and on budget.</p>
  </section>

  <section class="offer-box">
    <h2 class="offer-headline">ATTENTION BUILDERS!</h2>
    <p class="offer-question">Do you require top quality craftsman built Closets and Storage Systems?</p>
    <ul class="needs-list">
      <li>You need the same high quality in the closets that you provide in the rest of the home.</li>
      <li>You need someone that will be on time and stay within the budget.</li>
      <li>You need design options, color choices, and detailed plans to review with the homeowner.</li>
    </ul>
    <p class="call-line">Call Mark or Daniel<br>at Harbor Closets.</p>
  </section>

  <div class="brand-card">
    <div class="brand-mark"></div>
    <div class="brand-name">Harbor Closets<br>and Storage Systems</div>
  </div>

  <div class="phone-bar">
    <svg class="icon-badge" viewBox="0 0 46 46" aria-hidden="true">
      <circle cx="23" cy="23" r="22" fill="#ffffff"/>
      <path d="M16 11c2 0 3 4 3.5 6 .3 1.3-1.6 2.3-1.6 3 .8 3 3.3 5.6 6.2 6.6.8.2 1.6-1.8 3-1.5 2 .5 5.8 1.6 5.8 3.6 0 2.2-2.6 4.3-5 4.3C19 33 11 25 11 16c0-2.4 2.6-5 5-5z" fill="#c8141c"/>
    </svg>
    <span class="phone-number">208-555-0147</span>
  </div>

  <div class="web-bar">
    <svg class="icon-badge" viewBox="0 0 46 46" aria-hidden="true">
      <circle cx="23" cy="23" r="22" fill="#ffffff"/>
      <rect x="12" y="13" width="22" height="15" rx="1.5" fill="none" stroke="#0f1a45" stroke-width="3"/>
      <rect x="20" y="29" width="6" height="4" fill="#0f1a45"/>
      <rect x="16" y="32" width="14" height="3" fill="#0f1a45"/>
    </svg>
    <span class="web-address">www.harborclosetsandstoragesystems.com</span>
  </div>
</div>
</body>
</html>
```